Property development business card design

New build residential property developers. I want a professional look but customer friendly so not too corporate. I'm not sure what logo will look best so open to designs with either. Thank you

Also i don't want both names on one card its 2 names for 2 different cards but with the same design.

Industry/Entity Type

Residential

Contact Information for Business Card

TRW Developments Ltd,
58 Fennick Lane,
Ipswich,
Suffolk,
IP7 2DX

Property Research Manager
Judith Penrow

Managing Director
Dermot Aldwick

```html
<!DOCTYPE html>
<html lang="en">
<head>
<meta charset="utf-8">
<title>TRW Developments – Business Card</title>
<link rel="stylesheet" href="https://fonts.googleapis.com/css2?family=Open+Sans:wght@400;600;700&display=swap">
<style>
  :root {
    --page: #e9ebee;
    --navy: #0d3f66;
    --blue-deep: #1b5f93;
    --blue-light: #5aa6df;
    --brand-blue: #1a6fb5;
    --brand-green: #8cc63f;
    --ink: #333a40;
    --grey: #7d8186;
    --paper: #ffffff;
  }
  * { box-sizing: border-box; margin: 0; padding: 0; }
  html, body { width: 1200px; height: 784px; overflow: hidden; }
  body {
    background: var(--page);
    font-family: "Open Sans", Arial, sans-serif;
    position: relative;
  }
  .card {
    position: absolute;
    width: 600px;
    height: 343px;
    border-radius: 4px;
    overflow: hidden;
    box-shadow: 0 6px 18px rgba(0,0,0,.18);
  }

  /* Front */
  .card-front { left: 40px; top: 48px; }
  .front-pattern {
    position: absolute; inset: 0;
    background:
      radial-gradient(circle at 85% 30%, rgba(120,190,240,.55), transparent 45%),
      linear-gradient(120deg, var(--navy) 0%, var(--blue-deep) 55%, var(--blue-light) 100%);
  }
  .front-brand {
    position: absolute; left: 0; right: 0; top: 92px;
    display: flex; flex-direction: column; align-items: center; gap: 16px;
  }
  .brand-dot {
    width: 92px; height: 92px; border-radius: 50%;
    background: #dfe6ec;
  }
  .front-name {
    color: var(--paper);
    font-weight: 600;
    font-size: 30px;
    letter-spacing: 1px;
    text-transform: uppercase;
  }

  /* Back */
  .card-back { left: 560px; top: 400px; background: var(--paper); }
  .holder {
    position: absolute; right: 26px; top: 18px; text-align: right;
  }
  .holder-name { color: var(--brand-blue); font-weight: 700; font-size: 19px; line-height: 1.2; }
  .holder-role { color: var(--ink); font-weight: 600; font-size: 12.5px; }
  .back-brand {
    position: absolute; left: 36px; top: 70px;
    display: flex; flex-direction: column; align-items: flex-start; gap: 10px;
  }
  .back-brand .brand-dot {
    width: 88px; height: 88px; margin-left: 40px;
    background: var(--brand-blue);
  }
  .back-name {
    color: var(--grey);
    font-weight: 600;
    font-size: 26px;
    letter-spacing: .5px;
    text-transform: uppercase;
  }
  .watermark {
    position: absolute; right: -30px; top: 78px;
    width: 200px; height: 200px; border-radius: 50%;
    background: rgba(26,111,181,.07);
  }
  .contact {
    position: absolute; left: 36px; top: 212px;
    list-style: none;
    color: var(--ink);
    font-size: 15px;
    line-height: 21px;
  }
  .contact li { display: flex; align-items: flex-start; gap: 8px; }
  .contact svg { width: 14px; height: 14px; margin-top: 4px; fill: var(--brand-blue); flex: none; }
  .contact .indent { padding-left: 22px; }
</style>
</head>
<body>

<section class="card card-front">
  <div class="front-pattern" role="img" aria-label="Blue background with a perspective pattern of light circles"></div>
  <div class="front-brand">
    <span class="brand-dot"></span>
    <span class="front-name">TRW Developments</span>
  </div>
</section>

<section class="card card-back">
  <div class="watermark"></div>
  <div class="holder">
    <p class="holder-name">Judith Penrow</p>
    <p class="holder-role">Property Research Manager</p>
  </div>
  <div class="back-brand">
    <span class="brand-dot"></span>
    <span class="back-name">TRW Developments</span>
  </div>
  <ul class="contact">
    <li>
      <svg viewBox="0 0 16 16"><path d="M3.6 1.2l2.3 2.6-1.3 1.9c.9 2 2.6 3.7 4.6 4.6l1.9-1.3 2.6 2.3-1.3 2.6C7.4 14 2 8.6 1.1 3.6z"/></svg>
      <span>173 482 906</span>
    </li>
    <li>
      <svg viewBox="0 0 16 16"><path d="M8 1a7 7 0 1 0 0 14A7 7 0 0 0 8 1zm0 1.5c.7 0 1.6 1.4 1.9 4H6.1C6.4 3.9 7.3 2.5 8 2.5zM2.6 7.2h2.1c0 .6 0 1.1.1 1.6H2.6a5.6 5.6 0 0 1 0-1.6zm3.5 2.3h3.8c-.3 2.6-1.2 4-1.9 4s-1.6-1.4-1.9-4zm5.2-.7c.1-.5.1-1 .1-1.6h2a5.6 5.6 0 0 1 0 1.6z"/></svg>
      <span>www.trwdevelopment.com</span>
    </li>
    <li>
      <svg viewBox="0 0 16 16"><path d="M1 3h14v10H1zm1.5 1.3v.3L8 8.5l5.5-3.9v-.3z"/></svg>
      <span>info@trwdevelopment.com</span>
    </li>
    <li>
      <svg viewBox="0 0 16 16"><path d="M8 1.5L1 7.5h2V14h3.8v-4h2.4v4H13V7.5h2z"/></svg>
      <span>58 Fennick Lane, Ipswich,</span>
    </li>
    <li class="indent"><span>Suffolk, IP7 2DX</span></li>
  </ul>
</section>

</body>
</html>
```